Business Card Design

Great brand name mattresses at bulk prices, quality affordable for everyone.

something relating to a mattress is important for the card please.

Industry/Entity Type

Business

Contact Information for Business Card

Tervo Mattress

Requirements
Must have
• something related to a mattress, its the only thing we sell… the logo is not mandatory but would like, i understand the logo does not have a mattress

```html
<!DOCTYPE html>
<html lang="en">
<head>
<meta charset="utf-8">
<title>Tervo Mattress — Business Card</title>
<link href="https://fonts.googleapis.com/css2?family=Didact+Gothic&family=Montserrat:wght@600;700&display=swap" rel="stylesheet">
<style>
  :root {
    --backdrop: #e9e9e9;
    --card: #ffffff;
    --yellow: #fbee1a;
    --ink: #2b2b2b;
    --ink-soft: #3c3c3c;
    --quilt-light: #f4f4f4;
    --quilt-mid: #d9d9db;
    --quilt-shade: #c6c6c9;
  }
  * { box-sizing: border-box; margin: 0; padding: 0; }
  html, body {
    width: 1200px; height: 1200px; overflow: hidden;
    background: var(--backdrop);
  }
  .canvas { position: relative; width: 1200px; height: 1200px; }

  .card {
    position: absolute;
    width: 945px; height: 540px;
    background: var(--card);
    overflow: hidden;
    box-shadow: 0 4px 18px rgba(0,0,0,.12);
  }
  .card--front { left: 60px; top: 40px; }
  .card--back  { left: 195px; top: 620px; }

  /* mattress imagery areas */
  .mattress-photo { position: absolute; }
  .card--front .mattress-photo {
    left: 300px; top: 0; width: 645px; height: 380px;
    background:
      linear-gradient(90deg, var(--card) 0%, rgba(255,255,255,0) 38%),
      linear-gradient(180deg, var(--quilt-light) 0%, var(--quilt-mid) 55%, var(--quilt-shade) 72%, var(--card) 100%);
  }
  .card--back .mattress-photo {
    inset: 0;
    background:
      linear-gradient(90deg, rgba(255,255,255,.85) 0%, rgba(255,255,255,.2) 45%, rgba(255,255,255,0) 100%),
      linear-gradient(180deg, #f7f7f7 0%, #ececee 40%, var(--quilt-mid) 75%, #cfcfd2 100%);
  }

  /* brand */
  .brand {
    position: absolute;
    display: flex; align-items: center; gap: 18px;
  }
  .card--front .brand { left: 48px; top: 90px; }
  .card--back  .brand { left: 170px; top: 130px; }
  .brand__dot {
    width: 64px; height: 64px; border-radius: 50%;
    background: var(--yellow);
    flex: none;
  }
  .brand__name {
    font-family: "Montserrat", sans-serif;
    font-weight: 700;
    font-size: 34px;
    color: var(--ink);
    white-space: nowrap;
  }

  /* contact */
  .contact {
    position: absolute; left: 82px; top: 290px;
    list-style: none;
    font-family: "Didact Gothic", sans-serif;
    font-size: 27px;
    color: var(--ink-soft);
    line-height: 34px;
  }
  .contact li { display: flex; align-items: center; gap: 18px; }
  .contact .icon { width: 20px; height: 20px; flex: none; }
  .contact .no-icon { width: 20px; flex: none; }

  /* yellow bands */
  .band {
    position: absolute; left: 0; right: 0;
    background: var(--yellow);
    color: var(--ink);
    display: flex; align-items: center; justify-content: center;
    text-transform: uppercase;
  }
  .band--address {
    top: 420px; height: 52px;
    padding-left: 300px;
    font-family: "Didact Gothic", sans-serif;
    font-size: 24px;
    letter-spacing: .5px;
  }
  .band--tagline {
    top: 305px; height: 128px;
    flex-direction: column;
    padding-left: 150px;
    font-family: "Montserrat", sans-serif;
    font-weight: 700;
    font-size: 26px;
    line-height: 34px;
    text-align: center;
  }
</style>
</head>
<body>
<div class="canvas">

  <section class="card card--front">
    <div class="mattress-photo" role="img" aria-label="Close-up of a white quilted pillow-top mattress"></div>
    <div class="brand">
      <span class="brand__dot"></span>
      <span class="brand__name">Tervo Mattress</span>
    </div>
    <ul class="contact">
      <li>
        <svg class="icon" viewBox="0 0 20 20"><path fill="#2b2b2b" d="M4 1.5l3 .3 1.4 4-2 1.6c1 2.2 2.8 4 5 5l1.6-2 4 1.4.3 3c-.3 1.6-1.6 2.7-3.2 2.5C7.300 16.500 3.500 12.700 1.500 6.700 1.300 5.100 2.400 1.800 4 1.500z"/></svg>
        <span>555-555-5555</span>
      </li>
      <li>
        <svg class="icon" viewBox="0 0 20 20"><rect x="1" y="4" width="18" height="12" fill="#2b2b2b"/><path d="M1.5 4.5l8.5 6.5 8.5-6.5" stroke="#fff" stroke-width="1.6" fill="none"/></svg>
        <span>email@email.com</span>
      </li>
      <li>
        <span class="no-icon"></span>
        <span>yourwebsite.com</span>
      </li>
    </ul>
    <div class="band band--address">Address will go here</div>
  </section>

  <section class="card card--back">
    <div class="mattress-photo" role="img" aria-label="Bright bedroom with a white mattress, pillows and a branch vase"></div>
    <div class="brand">
      <span class="brand__dot"></span>
      <span class="brand__name">Tervo Mattress</span>
    </div>
    <div class="band band--tagline">
      <span>Great brand name mattresses at bulk prices,</span>
      <span>quality affordable for everyone</span>
    </div>
  </section>

</div>
</body>
</html>
```